Verostel business card

Business card for sustainable investment company called "Verostel". Verostel is an exchange platform selling carbon credits between buyers and sellers. Carbon Credits are an environmental commodity for reducing global carbon emissions.

the card should obviously have our logo and the theme should be sustainability/environment mixed with a trading platform.

Contact Information for Business Card

Logo, Name, Title, Phone, Email

Colors
0054AA
0677BA
7BADD7
CADEEF
E8F1F8
0094D4
00A9DD
6FCCEA
C7EBF8
E9F6FB
00AB8E
00BBA5
67D7C9
C6EFE9
E9F9F6
59FF00
82FF00
B8FF75
E3FFCB
F4FFEA

```html
<!DOCTYPE html>
<html lang="en">
<head>
<meta charset="utf-8">
<title>Verostel business card</title>
<link href="https://fonts.googleapis.com/css2?family=Montserrat:wght@400;500;600;700&display=swap" rel="stylesheet">
<style>
  :root {
    --backdrop: #3a3a3a;
    --navy: #0b2a52;
    --navy-deep: #082246;
    --ink: #1d2a3d;
    --text: #2b3440;
    --cyan: #33d3ea;
    --blue: #1f7fe6;
    --azure: #2a8cf0;
    --paper: #ffffff;
    --rule: #3d4754;
  }
  * { margin: 0; padding: 0; box-sizing: border-box; }
  html, body {
    width: 1200px; height: 689px; overflow: hidden;
    background: var(--backdrop);
    font-family: "Montserrat", sans-serif;
  }
  .canvas {
    position: relative; width: 1200px; height: 689px;
    display: flex; align-items: center; justify-content: center; gap: 50px;
  }
  .card {
    position: relative; width: 520px; height: 297px; overflow: hidden;
    box-shadow: 0 14px 30px rgba(0,0,0,.35);
  }

  /* Front */
  .card-front {
    background: linear-gradient(160deg, var(--navy) 0%, var(--navy-deep) 100%);
    display: flex; align-items: center; justify-content: center;
  }
  .front-brand {
    font-weight: 700; font-size: 46px; letter-spacing: 2px;
    color: var(--cyan); text-transform: uppercase;
  }

  /* Back */
  .card-back { background: var(--paper); }
  .brand-band {
    position: absolute; left: 0; top: 96px; width: 72px; height: 30px;
    background: linear-gradient(90deg, var(--azure) 0%, rgba(42,140,240,.25) 100%);
  }
  .brand-row {
    position: absolute; left: 82px; top: 90px;
    display: flex; align-items: center; gap: 10px;
  }
  .brand-mark { width: 26px; height: 26px; background: var(--blue); }
  .brand-name {
    font-weight: 700; font-size: 31px; letter-spacing: 1px;
    color: var(--ink); text-transform: uppercase;
  }
  .address {
    position: absolute; right: 28px; top: 62px; text-align: right;
    font-size: 12.5px; line-height: 1.35; color: var(--text);
  }
  .divider {
    position: absolute; left: 150px; right: 28px; top: 142px;
    height: 1px; background: var(--rule);
  }
  .person { position: absolute; left: 40px; top: 168px; }
  .person-name {
    font-weight: 700; font-size: 20px; letter-spacing: .5px;
    color: var(--blue); text-transform: uppercase;
  }
  .person-title { font-size: 12.5px; color: var(--text); margin-top: 1px; }
  .person-rule { width: 120px; height: 1px; background: var(--rule); margin: 8px 0 7px; }
  .contact-list { list-style: none; }
  .contact-item {
    display: flex; align-items: center; gap: 8px;
    font-size: 13px; line-height: 1.4; color: var(--text);
  }
  .contact-icon { width: 11px; height: 11px; flex: none; }
</style>
</head>
<body>
<main class="canvas">
  <section class="card card-front" aria-label="Card front">
    <span class="front-brand">Verostel</span>
  </section>

  <section class="card card-back" aria-label="Card back">
    <div class="brand-band"></div>
    <div class="brand-row">
      <span class="brand-mark"></span>
      <span class="brand-name">Verostel</span>
    </div>

    <address class="address">
      1420 Alder Creek Road<br>
      Fairview, Oregon 97024<br>
      www.verostel.com
    </address>

    <div class="divider"></div>

    <div class="person">
      <div class="person-name">Daniel Marsh</div>
      <div class="person-title">Managing Director</div>
      <div class="person-rule"></div>
      <ul class="contact-list">
        <li class="contact-item">
          <svg class="contact-icon" viewBox="0 0 12 12"><path d="M2.5 1l2 2.2-1 1.3c.8 1.6 2 2.8 3.6 3.6l1.3-1 2.1 2-1.2 1.8C5.6 10.6 1.4 6.4 1 2.2z" fill="#1fb3e0"/></svg>
          555-214-7380
        </li>
        <li class="contact-item">
          <svg class="contact-icon" viewBox="0 0 12 12"><rect x="3" y="0.8" width="6" height="10.4" rx="1.2" fill="none" stroke="#1fb3e0" stroke-width="1.2"/><circle cx="6" cy="9.3" r=".7" fill="#1fb3e0"/></svg>
          555-309-6142
        </li>
        <li class="contact-item">
          <svg class="contact-icon" viewBox="0 0 12 12"><rect x="0.8" y="2.2" width="10.4" height="7.6" fill="#1fb3e0"/><path d="M1 2.6l5 4 5-4" fill="none" stroke="#fff" stroke-width="1"/></svg>
          info@verostel.com
        </li>
      </ul>
    </div>
  </section>
</main>
</body>
</html>
```